"Cork Hollow Excursions" is a top notch Santa Barbara County Wine Tour company.

We provide scenic, boutique and custom wine tours. I need the card to be clean and classy. I will provide our logo. I would like the logo to cover the back side of the card as an option and would like to see a couple color options other then our signature green and gold. I would like to see some creative options and let the designers come up with options.
I need cards for myself and my team. The final design should communicate "An authentic and boutique wine tour experience"
Please use my website for reference www.corkhollowexcursions.com

Target Market(s)

We have a wide range of clients from millennials to baby boomers

Industry/Entity Type

Tour

Contact Information for Business Card

Contact info:
Dale Munford
805-291-6384
info@corkhollowexcursions.com
corkhollowexcursions.com

Colors

Designer to choose colors to be used in the design.

Requirements
Must have
• my logo
Nice to have
• *I would like to have the backside side with the logo and the company statement
• "An authentic and boutique wine tour experience" as an option.
• *I would also like to see what the designers can create!
• *I would like to see an option that incorporates or social: snapgrid, rovia, route scout
Should not have
• I do not want it too busy.

```html
<!DOCTYPE html>
<html lang="en">
<head>
<meta charset="utf-8">
<title>Cork Hollow Excursions – Business Card</title>
<link rel="stylesheet" href="https://fonts.googleapis.com/css2?family=Roboto:wght@400;500&family=Roboto+Condensed:wght@700&display=swap">
<style>
  :root {
    --backdrop: #2b2b2b;
    --card-white: #f2f2f1;
    --vine-green: #256843;
    --vine-green-mid: rgba(37, 104, 67, 0.55);
    --vine-green-soft: rgba(37, 104, 67, 0.12);
    --vine-green-clear: rgba(37, 104, 67, 0);
    --gold: #a08566;
    --ink: #4a4a4a;
    --white: #ffffff;
  }
  * { margin: 0; padding: 0; box-sizing: border-box; }
  html, body {
    width: 1200px; height: 960px; overflow: hidden;
    background: var(--backdrop);
    font-family: "Roboto", Arial, sans-serif;
  }
  .canvas { position: relative; width: 1200px; height: 960px; }

  .card { position: absolute; width: 600px; height: 343px; overflow: hidden; }
  .card-front { left: 314px; top: 113px; background: var(--card-white); }
  .card-back  { left: 311px; top: 472px; background: var(--vine-green); }

  /* Front */
  .brand-mark {
    position: absolute; left: 16px; top: 106px; width: 250px; text-align: center;
  }
  .brand-name {
    font-size: 18px; font-weight: 400; color: var(--gold);
    letter-spacing: 0.5px; white-space: nowrap;
  }
  .brand-region {
    margin-top: 6px; font-size: 8px; letter-spacing: 3px; color: var(--vine-green);
    text-transform: uppercase; white-space: nowrap;
  }
  .landscape-art {
    position: absolute; right: 0; bottom: 0; width: 340px; height: 300px;
    background: radial-gradient(ellipse 100% 100% at 100% 100%,
      var(--vine-green) 0%, var(--vine-green) 40%,
      var(--vine-green-mid) 60%, var(--vine-green-soft) 82%,
      var(--vine-green-clear) 100%);
  }
  .contact-block { position: absolute; left: 41px; top: 228px; }
  .person-name {
    font-family: "Roboto Condensed", "Arial Narrow", sans-serif;
    font-weight: 700; font-size: 21px; color: var(--vine-green);
    text-transform: uppercase; margin-bottom: 8px;
  }
  .contact-line {
    display: flex; align-items: center; gap: 9px;
    font-size: 14.5px; color: var(--ink); height: 19.5px;
  }
  .contact-line svg { width: 13px; height: 13px; fill: var(--vine-green); flex: none; }

  /* Back */
  .social-list {
    position: absolute; right: 30px; top: 38px; display: flex; gap: 10px;
    list-style: none;
  }
  .social-item {
    display: flex; align-items: center; gap: 4px;
    font-size: 10px; color: var(--white);
  }
  .social-item::before {
    content: ""; width: 9px; height: 9px; background: var(--white); border-radius: 2px;
  }
  .back-brand {
    position: absolute; left: 0; right: 0; top: 140px; text-align: center;
    font-size: 34px; font-weight: 400; color: var(--white); letter-spacing: 0.5px;
  }
  .tagline {
    position: absolute; left: 0; right: 0; top: 293px; text-align: center;
    font-size: 14.5px; color: var(--white);
  }
</style>
</head>
<body>
<main class="canvas">

  <section class="card card-front" aria-label="Card front">
    <div class="landscape-art" role="img" aria-label="Green vineyard landscape with hills and a rising sun"></div>

    <div class="brand-mark">
      <div class="brand-name">Cork Hollow Excursions</div>
      <div class="brand-region">Santa Barbara County</div>
    </div>

    <div class="contact-block">
      <h1 class="person-name">Dale Munford</h1>
      <div class="contact-line">
        <svg viewBox="0 0 24 24" aria-hidden="true"><path d="M6.6 10.8a15.1 15.1 0 0 0 6.6 6.6l2.2-2.2a1 1 0 0 1 1-.25 11.4 11.4 0 0 0 3.6.57 1 1 0 0 1 1 1V20a1 1 0 0 1-1 1A17 17 0 0 1 3 4a1 1 0 0 1 1-1h3.5a1 1 0 0 1 1 1c0 1.25.2 2.45.57 3.57a1 1 0 0 1-.25 1z"/></svg>
        <span>805-291-6384</span>
      </div>
      <div class="contact-line">
        <svg viewBox="0 0 24 24" aria-hidden="true"><path d="M2 5h20v14H2zM3.5 6.5 12 12.5l8.5-6z" fill-rule="evenodd"/></svg>
        <span>info@corkhollowexcursions.com</span>
      </div>
      <div class="contact-line">
        <svg viewBox="0 0 24 24" aria-hidden="true"><circle cx="12" cy="12" r="10"/></svg>
        <span>corkhollowexcursions.com</span>
      </div>
    </div>
  </section>

  <section class="card card-back" aria-label="Card back">
    <ul class="social-list">
      <li class="social-item">snapgrid</li>
      <li class="social-item">route scout</li>
      <li class="social-item">rovia</li>
    </ul>
    <div class="back-brand">Cork Hollow Excursions</div>
    <p class="tagline">An authentic &amp; boutique wine tour experience</p>
  </section>

</main>
</body>
</html>
```